Powerpoint and Word template required

We need PowerPoint and Word templates for all of our company branded materials and stationary. We have recently rebranded our website and would like something that is reflective of our new corporate branding. A sample of some of the documents we have created recently are attached and our website is below

http://lorventamedical.com.au/

The word template will be used for all letters we send to clients and customers and we think we want the logo and ISO 9001 cert to only appear on the first page.

The powerpoint template has to be flexible as we use this for both marketing and training purposes. I have attached a couple of samples of the types of documents we create and note that these are very basic / crude and we would be looking for something that is a significant improvement on these

In the powerpoint template it would be good to have lots of standard layouts within the template, e.g. different 'standard layouts for multiple elements on a page including pictures and text etc.
Updates

Project Deadline Extended
Reason: Still looking for a professional yet modern template and important to us that we can see more tan just a title slide and the layout of the other slide master slides is very important to us. Many thanks, Doug

Industry/Entity Type

Healthcare

Font styles to use
Sans Serif

Colors
33a6d7

Requirements
Must have
• Templates must be versatile for use; powerpoint template must be able to be used for training materials and weel as marketing / pitch books.
• Word template must be able to be used as a basis for our corporate letter head through to RFP response type documents as well as Reference / Operating manual type of documents
• In terms of the design it must be consistent with our new corporate image which is best represented by our new website design; www.lorventamedical.com

```html
<!DOCTYPE html>
<html lang="en">
<head>
<meta charset="utf-8">
<title>Lorventa Healthcare Letterhead</title>
<link href="https://fonts.googleapis.com/css2?family=Roboto+Condensed:wght@400;700&display=swap" rel="stylesheet">
<style>
  :root {
    --brand-blue: #2b80c5;
    --footer-blue: #2a7fc4;
    --ink: #1f1f1f;
    --rule: #9a9a9a;
    --paper: #fbfbfb;
    --white: #ffffff;
  }
  * { margin: 0; padding: 0; box-sizing: border-box; }
  html, body { width: 927px; height: 1200px; overflow: hidden; background: var(--paper); }
  body { font-family: "Roboto Condensed", "Arial Narrow", sans-serif; color: var(--ink); }
  .letterhead { position: relative; width: 927px; height: 1200px; background: var(--paper); }

  .cert-badge { position: absolute; left: 30px; top: 20px; width: 79px; height: 59px; background: var(--brand-blue); }

  .brand { position: absolute; right: 26px; top: 28px; display: flex; align-items: center; gap: 10px; }
  .brand-mark { width: 40px; height: 40px; background: var(--brand-blue); }
  .brand-name { font-size: 44px; font-weight: 700; color: var(--brand-blue); line-height: 1; }

  .header-rule { position: absolute; left: 30px; right: 24px; top: 91px; height: 1px; background: var(--rule); }

  .recipient { position: absolute; left: 48px; top: 162px; color: var(--brand-blue); font-weight: 700; font-size: 17px; line-height: 32px; }

  .letter-body { position: absolute; left: 48px; top: 290px; width: 835px; font-size: 17.4px; line-height: 30.7px; }
  .salutation { margin-bottom: 31px; }
  .letter-body p.copy { margin-bottom: 32px; }

  .footer { position: absolute; left: 0; bottom: 0; width: 927px; height: 109px; background: var(--footer-blue); color: var(--white); text-align: center; font-weight: 700; }
  .footer-address { position: absolute; top: 22px; width: 100%; font-size: 18px; }
  .footer-contact { position: absolute; top: 60px; width: 100%; font-size: 19px; letter-spacing: 0.2px; }
  .footer-contact .sep { margin: 0 9px; }
</style>
</head>
<body>
<main class="letterhead">
  <div class="cert-badge" role="img" aria-label="Certification badge"></div>

  <div class="brand">
    <span class="brand-mark"></span>
    <span class="brand-name">Lorventa</span>
  </div>

  <div class="header-rule"></div>

  <address class="recipient" style="font-style:normal">
    To,<br>Branch Manager<br>Australia
  </address>

  <section class="letter-body">
    <p class="salutation">Dear,</p>
    <p class="copy">Lorem Ipsum is simply dummy text of the printing and typesetting industry. Lorem Ipsum has been the industry's standard dummy text ever since the 1500s, when an unknown printer took a galley of type and scrambled it to make a type specimen book. It has survived not only five centuries, but also the leap into electronic typesetting, remaining essentially unchanged. It was popularised in the 1960s with the release of Letterform sheets containing Lorem Ipsum passages, and more recently with desktop publishing software like Pagewright Studio including versions of Lorem Ipsum.</p>
    <p class="copy">Lorem Ipsum is simply dummy text of the printing and typesetting industry. Lorem Ipsum has been the industry's standard dummy text ever since the 1500s, when an unknown printer took a galley of type and scrambled it to make a type specimen book. It has survived not only five centuries, but also the leap into electronic typesetting, remaining essentially unchanged. It was popularised in the 1960s with the release of Letterform sheets containing Lorem Ipsum passages, and more recently with desktop publishing software like Pagewright Studio including versions of Lorem Ipsum.</p>
    <p class="copy">Lorem Ipsum is simply dummy text of the printing and typesetting industry. Lorem Ipsum has been the industry's standard dummy text ever since the 1500s, when an unknown printer took a galley of type and scrambled it to make a type specimen book. It has survived not only five centuries</p>
    <p class="copy">But also the leap into electronic typesetting, remaining essentially unchanged. It was popularised in the 1960s with the release of Letterform sheets containing Lorem Ipsum passages, and more recently with desktop publishing software like Pagewright Studio including versions of Lorem Ipsum.</p>
  </section>

  <footer class="footer">
    <div class="footer-address">4/18 Calloway Street, Brenfield, NSW 2185</div>
    <div class="footer-contact">Phone: (02) 9480 3721<span class="sep">|</span>www.lorventamedical.com.au<span class="sep">|</span>info@lorventamedical.com.au</div>
  </footer>
</main>
</body>
</html>
```